Web and Logo Design for eCommerce site

We're launching a sister brand and require a full design for the site.

The site must have an established feel and appeal to corporate and institutional buyers.
Updates

Just a note about the wireframe design:

The Search & Rescue / Coast Guard / VLDT, etc. in the header area aren't buttons or menu items, but rather just info (along the lines of a tagline).  Sort of a "who we serve" sort of thing.

Worth noting is that it's specifically geared towards LARGE BUYERS.  For example, a police force buying 200 headlamps and 85 pairs of gloves.  So they'll register + sign in and then add a bunch of items to a RFQ.

Aim for a professional, masculine design.

Target Market(s)

We will be selling outdoor gear to the military, law enforcement, fire and rescue and first responders.

Requirements
Must have
• We require:
- Logo (vector based)

Site:
- template page
* main site template, re-skinned version of our current site
* horizontal drop-down menu
- product listings page
* thumbnail view of products
- product details page
* including elements such as product image, color/size selector, descriptions and specs (again, based loosely on our current website)
- account management page
* illustrating basic data entry styles for text box, buttons, grid, etc.

The site needs to be given a responsive design, so 2 versions of each design should be presented for desktop + mobile views.

Additional funds are available if the designer is able to fully implement the designs into a responsive framework such as bootstrap.

Nice to have
• Clean, professional design similar to:

http://forces.trailkinwear.com/gov/accessories/gloves.html

http://bolt.morvanix.com/ProductFind.aspx?language=EN&category=Hardshell&subcat=Waterproof_Jackets

```html
<!DOCTYPE html>
<html lang="en">
<head>
<meta charset="utf-8">
<title>Ridgeway – Vector Helmet</title>
<link href="https://fonts.googleapis.com/css2?family=Open+Sans:wght@300;400;600&display=swap" rel="stylesheet">
<style>
:root{
  --ink:#2b2b2b;
  --topbar:#1f252c;
  --nav:#2a3037;
  --nav-dark:#1c2127;
  --olive:#a7ad55;
  --olive-dark:#5c6336;
  --olive-btn:#8f9a50;
  --red:#c8161d;
  --band:#d3e0e1;
  --panel:#f1f1f1;
  --line:#dcdcdc;
  --footer:#17110b;
  --link-red:#b5121b;
}
*{box-sizing:border-box;margin:0;padding:0}
html,body{width:1175px;height:1200px;overflow:hidden}
body{font-family:"Open Sans",Arial,sans-serif;color:var(--ink);background:#fff;position:relative}
.band{position:absolute;left:0;top:115px;width:1175px;height:482px;background:var(--band)}
.topbar{position:absolute;left:0;top:0;width:1175px;height:33px;background:var(--topbar)}
.serve{position:absolute;left:108px;top:10px;font-size:10.5px;color:#d6d9dc;letter-spacing:.1px}
.serve span{margin:0 10px}
.social{position:absolute;right:98px;top:6px;display:flex;gap:7px}
.social i{display:block;width:20px;height:20px;border-radius:50%;background:#fff}
.header{position:absolute;left:0;top:33px;width:1175px;height:82px;background:#fff}
.brand{position:absolute;left:110px;top:15px;display:flex;align-items:center;gap:10px}
.brand-mark{width:44px;height:44px;border-radius:50%;background:var(--olive-dark)}
.brand-name{font-size:30px;font-weight:600;color:var(--olive-dark);letter-spacing:1px;line-height:1}
.brand-tag{font-size:9.5px;color:var(--olive-dark);font-weight:600;letter-spacing:1px;margin-top:4px}
.contact{position:absolute;right:88px;top:33px;font-size:13.5px;color:#666;display:flex;align-items:center;gap:8px}
.contact svg{flex:none}
.nav{position:absolute;left:108px;top:115px;width:959px;height:41px;background:linear-gradient(var(--nav),var(--nav-dark));display:flex;align-items:center;padding-left:20px}
.nav a{font-size:13.5px;color:var(--olive);text-decoration:none;margin-right:28px;text-transform:uppercase}
.nav a.active{color:#fff}
.search{position:absolute;right:14px;top:8px;width:25px;height:24px;background:var(--olive-btn);display:flex;align-items:center;justify-content:center}
.panel{position:absolute;left:108px;top:161px;width:961px;height:724px;background:var(--panel);border:1px solid var(--line);border-radius:3px}
.crumbs{position:absolute;left:12px;top:14px;width:936px;height:36px;background:#fff;border:1px solid #e3e3e3;border-radius:3px;font-size:12.5px;padding:9px 11px}
.crumbs a{color:#222}
.crumbs span{margin:0 6px}
.gallery{position:absolute;left:12px;top:60px;width:439px;height:422px;background:#fff;border:1px solid #e3e3e3}
.hero{position:absolute;left:110px;top:30px;width:210px;height:215px;border-radius:50% 50% 10px 10px;background:radial-gradient(circle at 45% 35%,#ff6a3a,#e8401c 60%,#2a2a2a 100%)}
.gallery h2{position:absolute;top:283px;width:100%;text-align:center;font-size:16px;font-weight:600}
.thumbs{position:absolute;top:345px;left:72px;display:flex;align-items:center;gap:6px}
.thumbs .t{width:55px;height:55px;border:2px solid #ddd;padding:8px}
.thumbs .t.on{border-color:#555}
.thumbs .t div{width:100%;height:100%;border-radius:50% 50% 4px 4px}
.arrow{width:0;height:0;border-top:6px solid transparent;border-bottom:6px solid transparent}
.arrow.l{border-right:8px solid var(--olive-dark);margin-right:10px}
.arrow.r{border-left:8px solid var(--olive-dark);margin-left:10px}
.price{position:absolute;left:476px;top:72px;font-size:46px;font-weight:300;letter-spacing:-2px}
.opts{position:absolute;left:470px;top:146px;font-size:12.5px}
.row{display:flex;align-items:center;margin-bottom:16px}
.row label{width:100px;text-align:right;padding-right:12px}
.chip{background:#fff;border:1px solid #e2e2e2;padding:3px 9px;margin-right:6px;font-size:13px;color:#555}
.chip.c{padding:4px 12px;margin-right:10px}
.btn{font-size:19px;font-weight:300;color:#fff;padding:9px 16px;border-radius:2px;margin-right:6px}
.btn.cart{background:var(--red)}
.btn.wish{background:var(--olive-dark)}
.divider{position:absolute;left:465px;top:313px;width:486px;border-top:1px solid #ddd}
.meta{position:absolute;left:480px;top:337px;display:flex;gap:14px}
.meta .mk{width:68px;height:68px;border-radius:50%;background:var(--olive-dark);margin-top:8px}
.meta h3{font-size:24px;font-weight:300;margin-bottom:8px}
.meta p{font-size:13px;line-height:20px}
.tabs{position:absolute;left:32px;top:508px;display:flex;gap:13px}
.tab{height:38px;padding:8px 27px;font-size:16px;background:#2d343b;color:#fff}
.tab.on{background:#fff;color:#222;border:1px solid #e3e3e3;border-bottom:none;height:42px}
.content{position:absolute;left:16px;top:546px;width:935px;height:170px;background:#fff;border:1px solid #e3e3e3;padding:24px 22px;font-size:12.5px;line-height:18px;color:#555}
.mail{display:flex;align-items:center;gap:7px;margin-top:32px}
.mail a{color:var(--link-red)}
.footer{position:absolute;left:0;top:915px;width:1175px;height:285px;background:var(--footer);color:#fff}
.col{position:absolute;top:38px}
.col h4{font-size:16px;font-weight:600;margin-bottom:12px}
.col ul{list-style:none;font-size:12.5px;line-height:15.5px;color:#e8e8e8}
.news p{font-size:12.5px;color:#c9c9c9;line-height:19px;width:260px;margin-top:16px}
.news form{display:flex;margin-top:30px}
.news .in{width:188px;height:38px;background:#fff;color:#999;font-size:13px;padding:10px}
.news .go{width:61px;height:38px;background:#ccc;color:#333;font-size:15px;padding:9px 11px}
.map{width:257px;height:166px;background:linear-gradient(135deg,#e9e6df,#f1ecd2 50%,#e4e1d8);margin-top:6px}
.copy{position:absolute;bottom:20px;width:100%;text-align:center;font-size:13px}
</style>
</head>
<body>
<div class="band"></div>

<div class="topbar">
  <div class="serve">SEARCH &amp;RECUE<span>|</span>COAST GUARD<span>|</span>VLDT<span>|</span>FIRE<span>|</span>MILIATRY<span>|</span>LAW ENFORCEMENT</div>
  <div class="social"><i></i><i></i><i></i><i></i></div>
</div>

<header class="header">
  <div class="brand">
    <div class="brand-mark"></div>
    <div><div class="brand-name">Ridgeway</div><div class="brand-tag">RIDGEWAY OUTDOOR PRO SUPPLY</div></div>
  </div>
  <div class="contact">
    <svg width="18" height="18" viewBox="0 0 24 24"><path fill="#888" d="M6.6 10.8a15 15 0 0 0 6.6 6.6l2.2-2.2c.3-.3.7-.4 1-.2 1.1.4 2.3.6 3.6.6.6 0 1 .4 1 1V20c0 .6-.4 1-1 1A17 17 0 0 1 3 4c0-.6.4-1 1-1h3.5c.6 0 1 .4 1 1 0 1.3.2 2.5.6 3.6.1.3 0 .7-.2 1z"/></svg>
    Call (+) 0800.555.019
    <svg width="18" height="16" viewBox="0 0 24 20" style="margin-left:6px"><path fill="none" stroke="#888" stroke-width="2" d="M2 7h20l-3 11H5zM8 7l4-5 4 5"/></svg>
    (0 item) - $0.00 <span style="font-size:10px">▼</span>
  </div>
</header>

<nav class="nav">
  <a class="active">Rescue Gear</a><a>Footwear</a><a>Clothing</a><a>Tents Mats Sleeping Bags</a><a>Camping Gear</a><a>Snow Sports</a><a>Brand’s</a>
  <div class="search"><svg width="14" height="14" viewBox="0 0 14 14"><circle cx="5.5" cy="5.5" r="4" fill="none" stroke="#fff" stroke-width="2"/><path d="M8.5 8.5l4 4" stroke="#fff" stroke-width="2"/></svg></div>
</nav>

<main class="panel">
  <div class="crumbs"><a>Rescue Gear</a><span>&gt;</span><a>Helmet</a><span>&gt;</span><a>Vector Helmet</a></div>

  <section class="gallery">
    <div class="hero" role="img" aria-label="Orange rescue helmet with black chin strap"></div>
    <h2>Vector Helmet</h2>
    <div class="thumbs">
      <div class="arrow l"></div>
      <div class="t on"><div role="img" aria-label="Orange helmet" style="background:#e84a22"></div></div>
      <div class="t"><div role="img" aria-label="Grey helmet" style="background:#8a8a8a"></div></div>
      <div class="t"><div role="img" aria-label="Yellow helmet" style="background:#e0c24a"></div></div>
      <div class="t"><div role="img" aria-label="Red helmet" style="background:#d9302c"></div></div>
      <div class="arrow r"></div>
    </div>
  </section>

  <div class="price">$ 9.99</div>
  <div class="opts">
    <div class="row"><label>Select a Size</label><span class="chip">XS</span><span class="chip">S</span><span class="chip">M</span><span class="chip">L</span><span class="chip">XL</span></div>
    <div class="row"><label>Select a Color</label><span class="chip c">Orange</span><span class="chip c">Grey</span><span class="chip c">Yellow</span><span class="chip c">Red</span></div>
    <div class="row"><label>Quantity</label><span class="btn cart">Add to Cart</span><span class="btn wish">Add to Wishlist</span></div>
  </div>
  <div class="divider"></div>
  <div class="meta">
    <div class="mk"></div>
    <div><h3>Vector Helmet</h3><p>Weight 81 ils (37kgs)<br>Model # 0356</p></div>
  </div>

  <div class="tabs"><div class="tab on">Overview</div><div class="tab">Specs</div><div class="tab">Extended Specs</div></div>
  <div class="content">
    <p>It is a long established fact that a reader will be distracted by the readable content of a page when looking at its layout. The point of using Lorem Ipsum is that it has a more-or-less normal distribution of letters, as opposed to using 'Content here, content here', making it look like readable English. Many desktop publishing packages and web page editors now use Lorem Ipsum as their default model text, and a search for 'lorem ipsum' will uncover many web sites still in their infancy. Various versions have evolved over the years, sometimes by accident, sometimes on purpose (injected humour and the like).</p>
    <div class="mail"><svg width="17" height="12" viewBox="0 0 17 12"><rect width="17" height="12" fill="#c8161d"/><path d="M0 0l8.5 7L17 0" fill="none" stroke="#fff" stroke-width="1.3"/></svg><a>Email this product to a friend</a></div>
  </div>
</main>

<footer class="footer">
  <div class="col" style="left:120px"><h4>Navigation</h4><ul><li>Rescue Gear</li><li>Footwear</li><li>Clothing</li><li>Tents Mats</li><li>Sleeping Bags</li><li>Camping Gear</li><li>Snow Sports</li><li>Brands</li></ul></div>
  <div class="col" style="left:287px"><h4>Products</h4><ul><li>Rescue Gear</li><li>Footwear</li><li>Clothing</li><li>Tents Mats</li><li>Sleeping Bags</li><li>Camping Gear</li><li>Snow Sports</li><li>Brands</li></ul></div>
  <div class="col news" style="left:444px"><h4>Get informed for our Special offers</h4><p>Get the best and most interesting discount offers via email.</p><form><div class="in">you@example.com</div><div class="go">Enter</div></form></div>
  <div class="col" style="left:778px;top:32px"><h4 style="margin-left:7px">Map</h4><div class="map" role="img" aria-label="Street map showing store location"></div></div>
  <div class="copy">CopyRight © 2014 RIDGEWAY All Received</div>
</footer>
</body>
</html>
```